Need a book cover design for a Lumora Book

Book has a long title and sub title so lots of words to fit on the cover.

I can be flexible a bit with the sub title due to the length of it but ideally i can get a design that takes everything.

Here is the title:

Tidal Geology: The Roots of Erosion, Sedimentation, and Canyon Forming

Sub Title/Heading
An Easy Primer on Coastal Cliffs, Dune Drift, River Beds, and Delta Mapping Methods

```html
<!DOCTYPE html>
<html lang="en">
<head>
<meta charset="utf-8">
<title>Tidal Geology – Book Cover</title>
<link href="https://fonts.googleapis.com/css2?family=Barlow+Condensed:wght@600&family=Montserrat:wght@700&display=swap" rel="stylesheet">
<style>
  :root {
    --page-bg: #ffffff;
    --paper: #f1f1f1;
    --paper-edge: #e2e2e2;
    --title-grey: #4b4b4d;
    --tagline-red: #6e1a0c;
    --subtitle-grey: #5a5a5c;
    --fire-core: #fff36a;
    --fire-orange: #f07a12;
    --fire-red: #b8270b;
    --fire-dark: #1a0704;
    --stream-blue: #1fa6e8;
    --stream-deep: #0a2a5c;
    --night: #040a1c;
  }
  html, body {
    margin: 0;
    width: 1200px;
    height: 1200px;
    overflow: hidden;
    background: var(--page-bg);
  }
  .canvas {
    position: relative;
    width: 1200px;
    height: 1200px;
  }
  .cover {
    position: absolute;
    left: 220px;
    top: 30px;
    width: 760px;
    height: 1140px;
    overflow: hidden;
    background: var(--paper);
  }
  .cover-art-top {
    position: absolute;
    left: 0; top: 0;
    width: 100%; height: 360px;
    background:
      radial-gradient(circle at 17% 22%, var(--fire-core) 0%, #ffc21f 8%, var(--fire-orange) 22%, transparent 48%),
      linear-gradient(100deg, var(--fire-red) 0%, #7a1a06 45%, var(--fire-dark) 80%, #2a0c04 100%);
  }
  .cover-art-bottom {
    position: absolute;
    left: 0; bottom: 0;
    width: 100%; height: 320px;
    background:
      radial-gradient(ellipse at 75% 70%, var(--stream-blue) 0%, #1467b8 30%, transparent 65%),
      linear-gradient(180deg, var(--night) 0%, var(--stream-deep) 60%, #0e4f9c 100%);
  }
  .paper-band {
    position: absolute;
    left: 0; top: 0;
    width: 760px; height: 1140px;
  }
  .cover-text {
    position: absolute;
    left: 0; top: 348px;
    width: 100%;
    text-align: center;
  }
  .tagline {
    margin: 0;
    font-family: "Montserrat", sans-serif;
    font-weight: 700;
    font-size: 30px;
    line-height: 36px;
    letter-spacing: 1.5px;
    color: var(--tagline-red);
    text-transform: uppercase;
  }
  .title {
    margin: 4px 0 0;
    font-family: "Barlow Condensed", sans-serif;
    font-weight: 600;
    font-size: 168px;
    line-height: 138px;
    letter-spacing: 2px;
    color: var(--title-grey);
    text-transform: uppercase;
  }
  .title span { display: block; }
  .subtitle {
    margin: 14px 0 0;
    font-family: "Montserrat", sans-serif;
    font-weight: 700;
    font-size: 20px;
    line-height: 27px;
    letter-spacing: 0.3px;
    color: var(--subtitle-grey);
    text-transform: uppercase;
  }
</style>
</head>
<body>
<div class="canvas">
  <div class="cover">
    <div class="cover-art-top" role="img" aria-label="Photograph of a bright star burst with fiery orange energy filaments over a dark sky"></div>
    <div class="cover-art-bottom" role="img" aria-label="Photograph of glowing blue light streams flowing across a dark surface"></div>

    <svg class="paper-band" viewBox="0 0 760 1140" aria-hidden="true">
      <path fill="var(--paper-edge)"
        d="M0 318 L30 312 L62 320 L95 308 L130 316 L170 305 L210 314 L250 303 L290 311 L330 300 L372 309 L410 299 L452 307 L495 297 L540 305 L582 296 L625 304 L668 294 L712 302 L760 292
           L760 852 L720 860 L680 849 L640 858 L598 846 L555 856 L512 844 L470 853 L428 842 L385 851 L342 840 L300 849 L258 838 L215 848 L172 837 L130 846 L88 836 L45 845 L0 834 Z"/>
      <path fill="var(--paper)"
        d="M0 324 L28 318 L60 326 L96 314 L132 322 L168 311 L208 320 L248 309 L292 317 L332 306 L370 315 L412 305 L450 313 L496 303 L538 311 L584 302 L624 310 L670 300 L710 308 L760 298
           L760 846 L722 854 L678 843 L642 852 L596 840 L556 850 L510 838 L472 847 L426 836 L387 845 L340 834 L302 843 L256 832 L217 842 L170 831 L132 840 L86 830 L47 839 L0 828 Z"/>
    </svg>

    <div class="cover-text">
      <p class="tagline">The Roots of Erosion,<br>Sedimentation,<br>and Canyon Forming</p>
      <h1 class="title"><span>Tidal</span><span>Geology</span></h1>
      <p class="subtitle">An Easy Primer on Coastal Cliffs,<br>Dune Drift, River Beds, and Delta<br>Mapping Methods</p>
    </div>
  </div>
</div>
</body>
</html>
```